Marrowgate Auctions Business Cards Design Needed

I need a business card design that is modern looking - double sided (maybe just my logo on the back, but open to suggestions) - the overall design is up to you. I want it to be easy to read - not over the top flashy. I already have a company logo which I uploaded so that needs to be used. The colors of my logo are the colors I want on the card... so blue and gray (do need to match the logo colors).

Requirements
Must have
• Would like the card to be sleek, modern and easy to ready

```html
<!DOCTYPE html>
<html lang="en">
<head>
<meta charset="utf-8">
<title>Marrowgate Auctions Business Cards</title>
<link href="https://fonts.googleapis.com/css2?family=Open+Sans:wght@300;400;600;700&display=swap" rel="stylesheet">
<style>
  :root {
    --stage: #2a2b2e;
    --navy: #161b26;
    --navy-deep: #0f131b;
    --blue: #3a8fcf;
    --blue-dark: #2a74b0;
    --gray-text: #5a5d63;
    --gray-light: #8a8d92;
    --paper: #f4f4f4;
  }
  * { margin: 0; padding: 0; box-sizing: border-box; }
  html, body { width: 1200px; height: 900px; overflow: hidden; }
  body {
    background: var(--stage);
    font-family: "Open Sans", Arial, sans-serif;
    position: relative;
  }
  .card {
    position: absolute;
    left: 300px;
    width: 600px;
    height: 340px;
    border-radius: 22px;
    overflow: hidden;
  }
  .card-back {
    top: 80px;
    background: linear-gradient(160deg, #1d2330 0%, var(--navy) 55%, var(--navy-deep) 100%);
    display: flex;
    flex-direction: column;
    align-items: center;
    justify-content: center;
  }
  .brand-name {
    font-weight: 700;
    color: var(--blue);
    letter-spacing: 3px;
    text-transform: uppercase;
  }
  .card-back .brand-name { font-size: 34px; }
  .tagline {
    margin-top: 12px;
    font-size: 15px;
    color: var(--blue);
    letter-spacing: 0.5px;
  }
  .rule {
    margin-top: 14px;
    width: 90px;
    height: 2px;
    background: var(--blue);
  }
  .card-front {
    top: 480px;
    background: var(--paper);
  }
  .front-shapes { position: absolute; inset: 0; }
  .front-brand {
    position: absolute;
    left: 370px;
    top: 130px;
    width: 210px;
    text-align: center;
  }
  .front-brand .brand-name { font-size: 20px; line-height: 1.3; }
  .person {
    position: absolute;
    left: 42px;
    top: 78px;
  }
  .person-name {
    font-size: 26px;
    color: var(--gray-text);
    letter-spacing: 0.5px;
    line-height: 1;
  }
  .person-name .first { font-weight: 700; }
  .person-name .last { font-weight: 300; }
  .person-title {
    margin-top: 4px;
    font-size: 16px;
    color: var(--blue);
    letter-spacing: 1px;
  }
  .person .rule { margin-top: 8px; width: 80px; }
  .contacts {
    position: absolute;
    left: 60px;
    top: 170px;
    list-style: none;
  }
  .contacts li {
    display: flex;
    align-items: center;
    gap: 14px;
    height: 44px;
    font-size: 15px;
    color: var(--gray-text);
  }
  .contact-icon {
    width: 30px;
    height: 30px;
    border-radius: 50%;
    background: var(--blue);
    display: flex;
    align-items: center;
    justify-content: center;
    flex-shrink: 0;
  }
</style>
</head>
<body>

<section class="card card-back">
  <div class="brand-name">Marrowgate Auctions</div>
  <div class="tagline">Improving Charity Auctions Nationwide</div>
  <div class="rule"></div>
</section>

<section class="card card-front">
  <svg class="front-shapes" width="600" height="340" viewBox="0 0 600 340" aria-hidden="true">
    <polygon points="230,0 292,0 306,72" fill="var(--blue)"/>
    <polygon points="292,0 600,0 600,340 500,340 332,196 306,72" fill="var(--navy)"/>
    <polygon points="425,340 500,340 458,300" fill="var(--blue)"/>
    <polygon points="300,166 345,154 360,200 318,212" fill="var(--blue)"/>
    <polygon points="318,212 360,200 352,226" fill="var(--blue-dark)"/>
    <rect x="568" y="52" width="32" height="50" fill="var(--blue)"/>
  </svg>

  <div class="front-brand">
    <div class="brand-name">Marrowgate<br>Auctions</div>
  </div>

  <div class="person">
    <div class="person-name"><span class="first">WES</span> <span class="last">HARLAN</span></div>
    <div class="person-title">AUCTIONEER</div>
    <div class="rule"></div>
  </div>

  <ul class="contacts">
    <li>
      <span class="contact-icon">
        <svg width="16" height="16" viewBox="0 0 24 24"><path d="M6.6 10.8a15.1 15.1 0 0 0 6.6 6.6l2.2-2.2a1 1 0 0 1 1-.25 11.4 11.4 0 0 0 3.6.6 1 1 0 0 1 1 1V20a1 1 0 0 1-1 1A17 17 0 0 1 3 4a1 1 0 0 1 1-1h3.5a1 1 0 0 1 1 1c0 1.25.2 2.45.6 3.6a1 1 0 0 1-.25 1z" fill="#fff"/></svg>
      </span>
      702-555-0148
    </li>
    <li>
      <span class="contact-icon">
        <svg width="16" height="16" viewBox="0 0 24 24"><rect x="3" y="6" width="18" height="12" rx="1" fill="none" stroke="#fff" stroke-width="2"/><path d="M3 7l9 6 9-6" fill="none" stroke="#fff" stroke-width="2"/></svg>
      </span>
      marrowgateauctions@mail.com
    </li>
    <li>
      <span class="contact-icon">
        <svg width="16" height="16" viewBox="0 0 24 24" fill="none" stroke="#fff" stroke-width="1.8"><circle cx="12" cy="12" r="9"/><ellipse cx="12" cy="12" rx="4" ry="9"/><path d="M3 12h18M5 7h14M5 17h14"/></svg>
      </span>
      http://gavelharbor.com/
    </li>
  </ul>
</section>

</body>
</html>
```